Race car follow-up website needs web design

We are currently finalising a website which allows amateur and professional owners of race cars to track the running time of the car and all installed parts (drive shafts, gearbox etc.). The site is working for a technical point of view, but needs a nice design applied to it.

The website is made with Bootstrap 3.x and does not need a mobile skin. We target desktop and tablet users. This means that the delivered work should be easy to incorporate in the Bootstrap site that currently exists, from a technical point of view.

In attachment you can find all the screens that need skinning. If you think some stuff can be done better from a usability or design point of view (size of tables, placement of buttons etc.), do not hesitate to make a suggestion. We are open to positive criticism, and the current "base" design is not carved in stone. The colors currently used are basic Bootstrap so that can change too. There are no limits whatsoever, as long as the result looks good.

We have a big amount of racing/racecar/mechanic/pitbox related photo material that can be used, so do not hesitate to ask for material if needed.

The start page should be something along the lines of these sites:

https://plumvex.me/
http://quorvane.io/
https://teldrova.com/
http://www.mivostrel.com/

Or in words: a top navigation bar (as seen in the screenshots). A full-width image relevant to the content (racing related) with some text in overlay (A sort of slogan along the lines of "Let us track your parts" or "Parts tracking for you race or trackday car" ). Under that image there should then be a very high-level overview of what the website can be used for (In a few steps, with graphics/photos, schematics, showing driving the car, data transfer, management in the site.). This so the potential user can quickly see if it is of any interest to him/her.

Basically:

Drive --- Download data -- Get Alerted

each step should contain an "icon" representing what it is about, and a few lines of text explaining what is meant.

On that page (in the image part, or below the explanation) there should be 2 links (buttons). One leads to the pricing page, one to the registration page.

Of course this first page cannot be finalised until we give the complete details of the content, so please provide a high-level design and the person I work with will receive the detailed specs (the text for the different steps etc).

The other screens are (we think) self-explanatory. Please look at them in chronological order (they are prefixed 00 to 19)

There are screenshots of the manual. This page will also need to be styled (to match the rest of the site and to make the layout a bit more sexy). We will of course provide the original html file to this once the content needs to be finalised.

Besides the website, a mail template is required too. The site sends mails for:
- registration confirmation
- lost password
- alerts related to the car parts or the data files.

These mails should also have a professional looking skin (right now they are plain text)

Just to make things clear, if you think the base design we made is "crap", please suggest improvements (for instance, menu placement in the bottom, positioning of certain elements, tables that might be better off somewhere else, the car details on top that take too much screen real-estate etc. etc.). This site has been built by developers, not by designers. The only condition is that it should be technically possible in a reasonable amount of time using Bootstrap 3.x

Please provide the resources in such a way that a developer with web skills can directly implement them. So any slicing of graphics should be done by the designer. If you only provide us a good looking psd file we won't be able to do anything with that, unfortunately.

If you, as a designer, have a passion for sports cars, race cars, trackdays and/or GT car racing, this is of course a plus. The collaboration will be a lot easier if we speak the same "language".

Please provide at least a design of
- the start page
- the "car details" page
- one of the list modals
- one of the form modals

so we can at least know how the rest of the pages will look

The name is Pitlane Ledger.

Some pictures that can be used:

https://www.snapvelo.com/photos/58310472@K04/20581937466/
https://www.snapvelo.com/photos/58310472@K04/4815209367/
https://www.snapvelo.com/photos/58310472@K04/4812766058/
https://www.snapvelo.com/photos/58310472@K04/4801533729/
https://www.snapvelo.com/photos/58310472@K04/4763921850/
https://www.snapvelo.com/photos/58310472@K04/4706418592/
https://www.snapvelo.com/photos/58310472@K04/4594071683/
https://www.snapvelo.com/photos/58310472@K04/4361829074/
https://www.snapvelo.com/photos/58310472@K04/3958316247/
https://www.snapvelo.com/photos/58310472@K04/3927140568/
https://www.snapvelo.com/photos/58310472@K04/3915762839/
https://www.snapvelo.com/photos/58310472@K04/3915764901/
https://www.snapvelo.com/photos/58310472@K04/3890417352/
https://www.snapvelo.com/photos/58310472@K04/3885093716/
https://www.snapvelo.com/photos/58310472@K04/3885097284/
https://www.snapvelo.com/photos/58310472@K04/2081359647/
https://www.snapvelo.com/photos/58310472@K04/2398640513/
https://www.snapvelo.com/photos/58310472@K04/2486075129/
https://www.snapvelo.com/photos/58310472@K04/2323149876/
https://www.snapvelo.com/photos/58310472@K04/2323154902/

Basically you take whatever you want from this guy’s photo stream:
https://www.snapvelo.com/photos/58310472@K04/

I know him personally so there should be no copyright issues.

Most users of the site will run so called "GT" cars (Valdorni, Castruzzo etc.), so please refrain from using (or referencing) open wheelers, F1, LMP etc.

There is a logo contest too: http://gigs.pixelbazaar.com/gig.aspx?id=837461

I just updated the brief with some more info and images you can use.

I have updated the brief. This is added: for the first screen, the schematics are explained in a bit more detail: Basically: Drive ---> Download data --> Get Alerted each step should contain an "icon" representing what it is about, and a few lines of text explaining what is meant.

Dear designers, As we have received numerous remarks about our contest from you and your colleagues we have contacted PixelBazaar to solve the situation. This contest will be split into two different contests. One logo design contest for $400 and one website design contest for the $1480. Everyone who has submitted logos can of course participate with those logos in the logo design contest (there are a few that we like, which have been submitted). We are very sorry for the inconvenience we might have caused, and if you want to redraw your designs already submitted because of this we will fully understand this, but we hope this decision will make things clearer for everyone participating. As soon as matters are changed we will send you all a new message with the updated information. Thanks for your understanding. Morlek BVBA

The logo contest has been created: http://gigs.pixelbazaar.com/gig.aspx?id=837461

Reason: Because of the split in webdesign / logo the deadline has been extended so non-logo webdesigners can participate too. Logo project: http://gigs.pixelbazaar.com/gig.aspx?id=837461

The pricing page has been added in the screenshots section

Trackday enthousiasts, race car owners, race teams.

• No video
No huge "footer" with a lot of links to navigate the site, since there will be very litte content.
No references to non-GT type cars (so no F1, no Series Quelmont, no LMP1/LMP2) or street cars.

```html
<!DOCTYPE html>
<html lang="en">
<head>
<meta charset="utf-8">
<title>Pitlane Ledger — Let us track your parts</title>
<link rel="stylesheet" href="https://fonts.googleapis.com/css2?family=Montserrat:wght@300;400;600;700;800&family=Mulish:wght@400;600;700&display=swap">
<style>
  :root{
    --ink:#1e1e1e;
    --ink-soft:#2b2b2b;
    --paper:#ffffff;
    --text:#2a2a2a;
    --muted:#8a8a8a;
    --footer-bg:#efefef;
    --hero-sky:#cbb890;
    --hero-warm:#a08a62;
    --hero-ground:#bdb3a3;
  }
  *{box-sizing:border-box;margin:0;padding:0}
  html,body{width:1200px;height:1177px;overflow:hidden;background:var(--paper)}
  body{position:relative;font-family:"Mulish",Arial,sans-serif;color:var(--text)}

  .hero{position:absolute;left:0;top:0;width:1200px;height:742px;
    background:
      radial-gradient(ellipse 520px 260px at 880px 450px, rgba(240,236,228,.55), rgba(240,236,228,0) 70%),
      linear-gradient(180deg,#e9e2cf 0%,var(--hero-sky) 18%,var(--hero-warm) 42%,#9b8e76 55%,var(--hero-ground) 72%,#cfc8bc 100%);}

  .brand{position:absolute;left:124px;top:48px;display:flex;align-items:center;gap:14px}
  .brand-mark{width:66px;height:66px;background:var(--ink);border:5px solid var(--paper)}
  .brand-name{font-family:"Montserrat",Arial,sans-serif;font-weight:800;font-size:31px;line-height:31px;color:var(--ink);letter-spacing:.5px}

  .topbar{position:absolute;left:398px;top:47px;width:678px;height:67px}
  .nav{position:absolute;left:682px;top:70px;display:flex;align-items:center;font-family:"Montserrat",Arial,sans-serif;font-size:14px;color:var(--paper)}
  .nav a{color:var(--paper);text-decoration:none}
  .nav .sep{margin:0 24px;opacity:.8;font-size:12px}
  .nav .register{position:absolute;left:299px;top:-6px;border:2px solid #9a9a9a;padding:4px 9px;white-space:nowrap}

  .hero-copy{position:absolute;left:127px;top:316px;width:430px;color:var(--paper);text-shadow:0 1px 3px rgba(0,0,0,.35)}
  .hero-title{font-family:"Montserrat",Arial,sans-serif;font-size:30px;font-weight:300;letter-spacing:.3px;white-space:nowrap}
  .hero-title strong{font-weight:800}
  .hero-text{margin-top:14px;font-size:14.5px;line-height:21.5px;font-weight:600}

  .btn{position:absolute;height:40px;font-family:"Montserrat",Arial,sans-serif;font-weight:700;font-size:14px;color:var(--paper);display:flex;align-items:center;justify-content:center;text-decoration:none}
  .btn svg{position:absolute;left:0;top:0}
  .btn span{position:relative}
  .btn-pricing{left:232px;top:460px;width:131px}
  .btn-register{left:384px;top:460px;width:170px}
  .btn-more{left:534px;top:1053px;width:130px}

  .band{position:absolute;left:0;top:742px;width:1200px;height:36px;background:var(--ink)}
  .steps{position:absolute;left:0;top:690px;width:1200px;height:130px}
  .step{position:absolute;top:762px;text-align:center;color:var(--paper);font-family:"Montserrat",Arial,sans-serif;font-size:16px;line-height:21px;font-weight:400;letter-spacing:.3px;white-space:nowrap}
  .step strong{font-weight:700}

  .welcome{position:absolute;left:0;top:864px;width:1200px;text-align:center}
  .welcome h1{font-family:"Montserrat",Arial,sans-serif;font-weight:400;font-size:30px;color:var(--ink);letter-spacing:.2px}
  .welcome h1 strong{font-weight:700}
  .welcome p{width:780px;margin:22px auto 0;font-size:14.5px;line-height:21.7px;color:var(--text)}

  .footer{position:absolute;left:0;top:1128px;width:1200px;height:49px;background:var(--footer-bg);font-size:11px;color:var(--muted)}
  .footer-links{position:absolute;left:126px;top:18px;font-weight:700}
  .footer-links a{color:var(--muted);text-decoration:none}
  .copyright{position:absolute;left:519px;top:18px}
  .social{position:absolute;left:905px;top:16px;display:flex;gap:5px}
  .social span{width:18px;height:16px;border:1px solid #b0b0b0}
  .footer-brand{position:absolute;left:964px;top:11px;display:flex;align-items:center;gap:8px}
  .footer-brand i{width:24px;height:24px;background:#b3b3b3}
  .footer-brand b{font-family:"Montserrat",Arial,sans-serif;font-weight:800;font-size:13px;line-height:13px;color:#b3b3b3}
</style>
</head>
<body>

<section class="hero" role="img" aria-label="Photo: white sports coupe parked on concrete in front of a stadium wall under a warm sunset sky"></section>

<header>
  <div class="brand">
    <div class="brand-mark"></div>
    <div class="brand-name">PITLANE<br>LEDGER</div>
  </div>
  <svg class="topbar" width="678" height="67" viewBox="0 0 678 67">
    <rect x="50" y="0" width="628" height="67" fill="#ffffff"/>
    <polygon points="22,8 678,8 678,59 2,59" fill="#1e1e1e"/>
    <polygon points="30,0 44,0 26,67 12,67" fill="#ffffff"/>
    <polygon points="42,0 56,0 38,67 24,67" fill="#1e1e1e"/>
  </svg>
  <nav class="nav">
    <a href="#">Home</a><span class="sep">|</span>
    <a href="#">My Cars</a><span class="sep">|</span>
    <a href="#">Contact Us</a>
    <a class="register" href="#">Register</a>
  </nav>
</header>

<div class="hero-copy">
  <h2 class="hero-title">LET US <strong>TRACK YOUR PARTS</strong></h2>
  <p class="hero-text">Lorem ipsum dolor sit amet, consectetuer adipiscing elit, sed diam nonummy nibh euismod tincidunt ut laoreet dolore magna aliquam erat volutpat. Ut wisi enim ad.</p>
</div>

<a class="btn btn-pricing" href="#">
  <svg width="131" height="44" viewBox="0 0 131 44"><rect x="17" y="0" width="114" height="44" fill="#fff"/><polygon points="10,4 122,4 122,38 0,38" fill="#1e1e1e"/></svg>
  <span>Pricing</span>
</a>
<a class="btn btn-register" href="#">
  <svg width="170" height="44" viewBox="0 0 170 44"><rect x="17" y="0" width="153" height="44" fill="#fff"/><polygon points="10,4 161,4 161,38 0,38" fill="#1e1e1e"/></svg>
  <span>Registeration</span>
</a>

<div class="band"></div>
<svg class="steps" width="1200" height="130" viewBox="0 0 1200 130">
  <rect x="250" y="0" width="706" height="10" fill="#fff"/>
  <polygon points="410,8 418,8 418,38 443,64 418,90 418,120 410,120 410,90 435,64 410,38" fill="#fff"/>
  <polygon points="600,8 608,8 608,38 633,64 608,90 608,120 600,120 600,90 625,64 600,38" fill="#fff"/>
  <polygon points="763,8 771,8 771,38 796,64 771,90 771,120 763,120 763,90 788,64 763,38" fill="#fff"/>
  <polygon points="950,8 956,8 956,38 981,64 956,90 948,90 973,64" fill="#fff"/>
  <polygon points="244,8 410,8 410,38 435,64 410,90 410,120 217,120 229,90" fill="#1e1e1e"/>
  <polygon points="418,8 600,8 600,38 625,64 600,90 600,120 418,120 418,90 443,64 418,38" fill="#1e1e1e"/>
  <polygon points="608,8 763,8 763,38 788,64 763,90 763,120 608,120 608,90 633,64 608,38" fill="#1e1e1e"/>
  <polygon points="771,8 950,8 950,38 975,64 950,90 950,120 771,120 771,90 796,64 771,38" fill="#1e1e1e"/>

  <g fill="none" stroke="#fff" stroke-width="2.4" stroke-linecap="round" stroke-linejoin="round">
    <path d="M311,32 l22,22 M333,32 l-22,22"/>
    <circle cx="310" cy="31" r="4"/>
    <circle cx="334" cy="55" r="3"/>
    <circle cx="511" cy="42" r="14"/>
    <path d="M511,34 v9 l-4,6"/>
    <rect x="676" y="37" width="26" height="20"/>
    <path d="M676,37 l13,11 l13,-11 M689,25 v13 M684,33 l5,5 l5,-5"/>
    <circle cx="862" cy="42" r="14"/>
    <path d="M855,50 a8,8 0 1 1 14,0 M862,47 l3,-9"/>
  </g>
</svg>
<div class="step" style="left:262px;width:120px">Keep Track of<br>Your <strong>Parts</strong></div>
<div class="step" style="left:441px;width:140px">Keep Track of<br>Your <strong>Lap Times</strong></div>
<div class="step" style="left:630px;width:120px">Get Alert<br><strong>Messages</strong></div>
<div class="step" style="left:793px;width:140px">Keep Track of<br><strong>Fuel Millage</strong></div>

<section class="welcome">
  <h1>Welcome to <strong>Pitlane Ledger</strong></h1>
  <p>Lorem ipsum dolor sit amet, consectetuer adipiscing elit, sed diam nonummy nibh euismod tincidunt ut laoreet dolore magna aliquam erat volutpat. Ut wisi enim ad minim.adipiscing elit, sed diam nonummy nibh euismod tincidunt ut laoreet dolore magna aliquam erat volutpat. Ut wisi enim ad minim.adipiscing elit, sed diam nonummy nibh euismod tincidunt ut laoreet dolore magna aliquam erat volutpat. Ut wisi enim ad minim.</p>
</section>

<a class="btn btn-more" href="#">
  <svg width="130" height="44" viewBox="0 0 130 44"><rect x="17" y="0" width="113" height="44" fill="#fff" stroke="#e4e4e4"/><polygon points="10,2 122,2 122,36 0,36" fill="#1e1e1e"/></svg>
  <span>Read More</span>
</a>

<footer class="footer">
  <div class="footer-links"><a href="#">Home</a> | <a href="#">Register</a> | <a href="#">My Cars</a> | <a href="#">Contact Us</a></div>
  <div class="copyright">©2013-2014, All rights Reserved</div>
  <div class="social"><span></span><span></span></div>
  <div class="footer-brand"><i></i><b>PITLANE<br>LEDGER</b></div>
</footer>

</body>
</html>
```